Business card for Mortgage broker business

I have already had the logo designed and am needing a great looking business card. My business focus is on servicing clients who may not be able to obtain finance through traditional lenders due to bad credit, short term employment or they just don't fit the banks profile. It needs to be professional, trust worthy but also have a caring fell about it.
I have provided files showing the green and black logo, the white logo(on white background so the file looks blank) and also a file with the white logo with a background of leaves that was made up which will probably be used for a website header.

Industry/Entity Type

Finance

Contact Information for Business Card

Marcus Dolbey
Managing Director, Accredited Finance Broker(AFB)
Po Box 287, Pakenham VIC 3810
marcus@kestrelfinance.com.au
www.kestrelfinance.com.au
0438 162 507

Requirements
Nice to have
• I have added a picture of myself as I would like to see some designs with the pic in it, but I'm not sure if I want it on there with the logo's or just the logo's

```html
<!DOCTYPE html>
<html lang="en">
<head>
<meta charset="utf-8">
<title>Kestrel Finance – Business Card</title>
<link href="https://fonts.googleapis.com/css2?family=Source+Sans+3:wght@400;600&display=swap" rel="stylesheet">
<style>
  :root {
    --brand-green: #0b6b3a;
    --text-dark: #2a2a2a;
    --card-white: #fbfbfb;
    --page-bg: #e9e9e7;
    --divider: #9a9a9a;
  }
  * { margin: 0; padding: 0; box-sizing: border-box; }
  html, body {
    width: 1200px;
    height: 900px;
    overflow: hidden;
    background: var(--page-bg);
    font-family: "Source Sans 3", "Myriad Pro", Arial, sans-serif;
  }
  .business-card {
    position: absolute;
    left: 275px;
    top: 250px;
    width: 650px;
    height: 400px;
    background: var(--card-white);
    border-radius: 14px;
    overflow: hidden;
    box-shadow: 0 2px 10px rgba(0,0,0,0.12);
  }
  .brand-mark {
    position: absolute;
    left: 0;
    right: 0;
    top: 80px;
    display: flex;
    justify-content: center;
    align-items: center;
    gap: 14px;
  }
  .brand-mark__dot {
    width: 26px;
    height: 26px;
    border-radius: 50%;
    background: var(--brand-green);
  }
  .brand-mark__name {
    font-size: 46px;
    font-weight: 600;
    color: var(--brand-green);
    letter-spacing: 0.5px;
  }
  .person {
    position: absolute;
    right: 343px;
    top: 234px;
    text-align: right;
    white-space: nowrap;
  }
  .person__name {
    font-size: 21px;
    font-weight: 600;
    color: var(--brand-green);
    line-height: 28px;
  }
  .person__title {
    font-size: 17px;
    color: var(--text-dark);
    line-height: 24px;
  }
  .person__web {
    font-size: 17px;
    color: var(--brand-green);
    line-height: 25px;
  }
  .divider {
    position: absolute;
    left: 325px;
    top: 245px;
    width: 1px;
    height: 62px;
    background: var(--divider);
  }
  .contact-list {
    position: absolute;
    left: 340px;
    top: 241px;
    list-style: none;
    white-space: nowrap;
  }
  .contact-list__item {
    display: flex;
    align-items: center;
    gap: 9px;
    font-size: 17px;
    color: var(--text-dark);
    line-height: 24px;
  }
  .contact-list__icon {
    width: 13px;
    height: 13px;
    fill: var(--brand-green);
    flex: none;
  }
  .address-band {
    position: absolute;
    left: 0;
    bottom: 0;
    width: 100%;
    height: 66px;
    background: var(--brand-green);
    color: #ffffff;
    font-size: 17px;
    display: flex;
    justify-content: center;
    align-items: center;
  }
</style>
</head>
<body>
  <div class="business-card">
    <div class="brand-mark">
      <span class="brand-mark__dot"></span>
      <span class="brand-mark__name">Kestrel Finance</span>
    </div>

    <div class="person">
      <p class="person__name">Marcus Dolbey</p>
      <p class="person__title">Managing Director</p>
      <p class="person__web">www.kestrelfinance.com.au</p>
    </div>

    <div class="divider"></div>

    <ul class="contact-list">
      <li class="contact-list__item">
        <svg class="contact-list__icon" viewBox="0 0 16 16" aria-hidden="true">
          <path d="M2 6c0-3 3-4 6-4s6 1 6 4v1h-3.5V5.5h-5V7H2z"/>
          <path d="M4 8h8l2 6H2z"/>
        </svg>
        <span>0438 162 507</span>
      </li>
      <li class="contact-list__item">
        <svg class="contact-list__icon" viewBox="0 0 16 16" aria-hidden="true">
          <rect x="4" y="1" width="8" height="5"/>
          <rect x="1" y="6" width="14" height="9" rx="1"/>
          <rect x="4" y="9" width="8" height="1.5" fill="#fbfbfb"/>
        </svg>
        <span>03 5941 2760</span>
      </li>
      <li class="contact-list__item">
        <svg class="contact-list__icon" viewBox="0 0 16 16" aria-hidden="true">
          <rect x="1" y="3" width="14" height="10"/>
          <path d="M1.5 3.5L8 9l6.5-5.5" fill="none" stroke="#fbfbfb" stroke-width="1.3"/>
        </svg>
        <span>marcus@kestrelfinance.com.au</span>
      </li>
    </ul>

    <div class="address-band">Po Box 287, Pakenham VIC 3810</div>
  </div>
</body>
</html>
```